Cedar Ridge Paving. Chip Seal Done Right

I need my card to have all my basic information on it. Keep it simple. Include web site, phone number and email address. Include phrase Chip Seal Done Right or Cedar Ridge’s Top Paving Company. Keep card simple. Include color and logo. Put all contact info on card. Make card simple and not complicated.
Updates

Here is infuriation yo out in business card

Mark T. Delgado
512.408.7316 cell phone
Markdelgado7@mailbrook.net
www.cedarridgepaving.net

Target Market(s)

Hill Country Texas USA

Industry/Entity Type

Road chip seal

Contact Information for Business Card

We chip seal roads for ranches and property owners

Font styles to use
Serif
Sans Serif
Decorative
Script

Colors
0054AA
0677BA
7BADD7
CADEEF
E8F1F8
EB3D1F
EC4F4E
F09395
F8D3D4
FCEDEE

Requirements
Must have
• Keep it simply
Nice to have
• Logo and all basic info

```html
<!DOCTYPE html>
<html lang="en">
<head>
<meta charset="utf-8">
<title>Cedar Ridge Paving — Business Card</title>
<link rel="stylesheet" href="https://fonts.googleapis.com/css2?family=Montserrat:wght@400;500;800&display=swap">
<style>
  :root {
    --backdrop: #e6e6e6;
    --navy: #0c1a4e;
    --red: #c81f2e;
    --ink: #2b2b2b;
    --rule: #b5b5b5;
    --paper: #ffffff;
  }
  * { margin: 0; padding: 0; box-sizing: border-box; }
  html, body {
    width: 1200px; height: 1200px; overflow: hidden;
    background: var(--backdrop);
    font-family: "Montserrat", Arial, sans-serif;
  }
  .sheet {
    width: 1200px; height: 1200px;
    display: flex; flex-direction: column; align-items: center; justify-content: center;
    gap: 60px;
  }
  .card {
    width: 880px; height: 503px; position: relative;
    box-shadow: 0 6px 18px rgba(0,0,0,.18);
  }
  /* Front */
  .card--front { background: var(--paper); display: flex; align-items: center; }
  .card--front .brand-side {
    width: 50%; height: 100%; display: flex; align-items: center; justify-content: center;
  }
  .divider { width: 1px; height: 170px; background: var(--rule); }
  .contact-side { flex: 1; padding-left: 60px; }
  .person { border-left: 5px solid var(--red); padding-left: 14px; margin-bottom: 26px; }
  .person__name { color: var(--red); font-weight: 500; font-size: 38px; letter-spacing: .5px; line-height: 1.05; }
  .person__role { color: var(--ink); font-size: 17px; letter-spacing: 1px; margin-top: 4px; }
  .contact-list { list-style: none; padding-left: 19px; }
  .contact-list li {
    display: flex; align-items: center; gap: 12px;
    color: var(--ink); font-size: 21px; margin-bottom: 12px;
  }
  .contact-list svg { width: 22px; height: 22px; flex: none; fill: var(--red); }
  /* Logo wordmark */
  .wordmark { display: flex; align-items: center; gap: 14px; }
  .wordmark__mark { width: 34px; height: 34px; background: var(--red); flex: none; }
  .wordmark__name {
    font-weight: 800; font-size: 34px; line-height: 1; color: var(--navy);
    text-transform: uppercase; letter-spacing: .5px;
  }
  /* Back */
  .card--back { background: linear-gradient(135deg, #0a1a52 0%, #13245e 55%, #0a1848 100%); }
  .card--back .wordmark { position: absolute; left: 150px; top: 180px; gap: 22px; }
  .card--back .wordmark__mark { width: 62px; height: 62px; }
  .card--back .wordmark__name { color: #ffffff; font-size: 62px; }
  .tagline {
    position: absolute; right: 70px; bottom: 70px;
    color: #ffffff; font-size: 34px; font-weight: 400; letter-spacing: 1px;
  }
</style>
</head>
<body>
<main class="sheet">
  <section class="card card--front" aria-label="Business card front">
    <div class="brand-side">
      <div class="wordmark">
        <span class="wordmark__mark"></span>
        <span class="wordmark__name">Cedar Ridge<br>Paving</span>
      </div>
    </div>
    <div class="divider"></div>
    <div class="contact-side">
      <div class="person">
        <p class="person__name">JOHN DOE</p>
        <p class="person__role">CEO | FOUNDER</p>
      </div>
      <ul class="contact-list">
        <li>
          <svg viewBox="0 0 24 24" aria-hidden="true"><path d="M6.6 10.8a15.1 15.1 0 0 0 6.6 6.6l2.2-2.2a1 1 0 0 1 1-.25 11.4 11.4 0 0 0 3.6.57 1 1 0 0 1 1 1V20a1 1 0 0 1-1 1A17 17 0 0 1 3 4a1 1 0 0 1 1-1h3.5a1 1 0 0 1 1 1c0 1.25.2 2.45.57 3.57a1 1 0 0 1-.25 1z"/></svg>
          000 000 0000
        </li>
        <li>
          <svg viewBox="0 0 24 24" aria-hidden="true"><path d="M2 5h20v14H2z M3.5 6.5 12 13l8.5-6.5" fill="var(--red)"/><path d="M3 6l9 7 9-7" fill="none" stroke="#fff" stroke-width="1.6"/></svg>
          contact@example.com
        </li>
        <li>
          <svg viewBox="0 0 24 24" aria-hidden="true"><circle cx="12" cy="12" r="10"/><g fill="none" stroke="#fff" stroke-width="1.3"><ellipse cx="12" cy="12" rx="4.5" ry="10"/><path d="M2 12h20M4 7h16M4 17h16M12 2v20"/></g></svg>
          www.example.com
        </li>
      </ul>
    </div>
  </section>

  <section class="card card--back" aria-label="Business card back">
    <div class="wordmark">
      <span class="wordmark__mark"></span>
      <span class="wordmark__name">Cedar Ridge<br>Paving</span>
    </div>
    <p class="tagline">CHIP SEAL DONE RIGHT</p>
  </section>
</main>
</body>
</html>
```